Tights Color Chart

We Need for a Webshop 3 or 4 different Color Charts to see the Colors of the Tights.

1 Color Chart only with this Colors: black/schwarz, white/weiss,
naturel/natur.

The other 3 or 4 Charts up to your Design!

Total 54 Colors.

The Language must be in English and German.
Each single Color Chart should have rounded Corners see attachment.

Thank you in advance
BEN

Target Market(s)

Woman, Webshop

Requirements
Must have
• the right Colors, English and German, for the Webshop

```html
<!DOCTYPE html>
<html lang="en">
<head>
<meta charset="utf-8">
<title>Tights Color Chart</title>
<link href="https://fonts.googleapis.com/css2?family=Arimo:wght@400&family=Kaushan+Script&display=swap" rel="stylesheet">
<style>
  :root {
    --page-bg: #ffffff;
    --band-bg: #f0f0f2;
    --panel-bg: #f8f8f8;
    --title: #6a2d91;
    --label-en: #1e1e1e;
    --label-de: #7a7a7a;
    --chip-edge: #dcdcdc;
  }
  html, body { margin: 0; padding: 0; overflow: hidden; }
  body { width: 1200px; height: 1116px; background: var(--page-bg); font-family: "Arimo", Arial, sans-serif; }
  .chart { position: relative; width: 1500px; height: 1395px; transform: scale(0.8); transform-origin: 0 0; }
  .chart-title {
    position: absolute; left: 0; right: 0; top: 22px; margin: 0; text-align: center;
    font-family: "Kaushan Script", cursive; font-weight: 400; font-size: 96px; color: var(--title);
    letter-spacing: 2px;
  }
  .basics-band { position: absolute; left: 0; top: 161px; width: 1500px; height: 132px; background: var(--band-bg); }
  .dark-panel { position: absolute; left: 920px; top: 293px; width: 580px; height: 1102px; background: var(--panel-bg); }
  .color { position: absolute; width: 83px; display: flex; flex-direction: column; align-items: center; }
  .swatch { width: 83px; height: 64px; border-radius: 10px; background: var(--c); box-sizing: border-box; }
  .swatch.light { border: 1px solid var(--chip-edge); }
  .name { margin-top: 8px; white-space: nowrap; text-align: center; font-size: 16px; line-height: 19px; color: var(--label-en); }
  .name span { color: var(--label-de); }
  .color.basic { width: 98px; }
  .color.basic .swatch { width: 98px; height: 75px; border-radius: 12px; }
  .color.basic .name { font-size: 18px; line-height: 22px; margin-top: 9px; }
</style>
</head>
<body>
<main class="chart">
  <h1 class="chart-title">Tights Color Chart</h1>

  <section class="basics-band">
    <div class="color basic" style="left:535px;top:15px"><div class="swatch" style="--c:#000000"></div><div class="name">black <span>/ schwarz</span></div></div>
    <div class="color basic" style="left:704px;top:15px"><div class="swatch light" style="--c:#ffffff"></div><div class="name">white <span>/ weiss</span></div></div>
    <div class="color basic" style="left:894px;top:15px"><div class="swatch" style="--c:#e2bea5"></div><div class="name">naturel <span>/ natur</span></div></div>
  </section>

  <div class="dark-panel"></div>

  <section class="light-colors">
    <div class="color" style="left:36px;top:324px"><div class="swatch light" style="--c:#ffffff"></div><div class="name">white /<br><span>weiss</span></div></div>
    <div class="color" style="left:143px;top:324px"><div class="swatch light" style="--c:#fdfdf4"></div><div class="name">cream /<br><span>creme</span></div></div>
    <div class="color" style="left:244px;top:324px"><div class="swatch light" style="--c:#fbfbf0"></div><div class="name">kalina /<br><span>kalina</span></div></div>
    <div class="color" style="left:347px;top:324px"><div class="swatch light" style="--c:#f6f6f1"></div><div class="name">ecru <span>/ ecru</span></div></div>
    <div class="color" style="left:463px;top:324px"><div class="swatch" style="--c:#eae9e4"></div><div class="name">perle <span>/ perle</span></div></div>
    <div class="color" style="left:581px;top:324px"><div class="swatch" style="--c:#e2e2e4"></div><div class="name">ash <span>/ asche</span></div></div>

    <div class="color" style="left:36px;top:449px"><div class="swatch" style="--c:#957670"></div><div class="name">cacao /<br><span>kakao</span></div></div>
    <div class="color" style="left:143px;top:449px"><div class="swatch" style="--c:#8f6c51"></div><div class="name">nugat /<br><span>nougat</span></div></div>
    <div class="color" style="left:244px;top:449px"><div class="swatch" style="--c:#b0876b"></div><div class="name">beige /<br><span>beige</span></div></div>
    <div class="color" style="left:347px;top:449px"><div class="swatch" style="--c:#e2bfa4"></div><div class="name">naturel /<br><span>natur</span></div></div>

    <div class="color" style="left:36px;top:582px"><div class="swatch" style="--c:#d98a82"></div><div class="name">salmon /<br><span>Lachs</span></div></div>
    <div class="color" style="left:143px;top:582px"><div class="swatch" style="--c:#f09a48"></div><div class="name">orange /<br><span>orange</span></div></div>

    <div class="color" style="left:36px;top:713px"><div class="swatch" style="--c:#b94b48"></div><div class="name">rosso /<br><span>rosso</span></div></div>
    <div class="color" style="left:143px;top:713px"><div class="swatch" style="--c:#b04457"></div><div class="name">lipstic /<br><span>rot</span></div></div>
    <div class="color" style="left:244px;top:713px"><div class="swatch" style="--c:#d94f5c"></div><div class="name">sorbet /<br><span>sorbet</span></div></div>
    <div class="color" style="left:347px;top:713px"><div class="swatch" style="--c:#da4e70"></div><div class="name">raspberry /<br><span>himbeer</span></div></div>

    <div class="color" style="left:36px;top:853px"><div class="swatch" style="--c:#ffa6d9"></div><div class="name">orchidea /<br><span>orchidea</span></div></div>
    <div class="color" style="left:143px;top:853px"><div class="swatch" style="--c:#ffa6d8"></div><div class="name">pink /<br><span>rosa</span></div></div>
    <div class="color" style="left:244px;top:853px"><div class="swatch" style="--c:#f4dbe5"></div><div class="name">rose /<br><span>hallrose</span></div></div>
    <div class="color" style="left:347px;top:853px"><div class="swatch light" style="--c:#fbf0f6"></div><div class="name">baby pink /<br><span>baby rose</span></div></div>
    <div class="color" style="left:463px;top:853px"><div class="swatch" style="--c:#d654a3"></div><div class="name">crocus /<br><span>Krokus</span></div></div>
    <div class="color" style="left:581px;top:853px"><div class="swatch" style="--c:#e77aae"></div><div class="name">lavende /<br><span>Lavendel</span></div></div>
    <div class="color" style="left:691px;top:853px"><div class="swatch" style="--c:#a34275"></div><div class="name">fuchsia /<br><span>fuchsia</span></div></div>
    <div class="color" style="left:797px;top:853px"><div class="swatch" style="--c:#974f6e"></div><div class="name">mulberry /<br><span>Maulbeere</span></div></div>

    <div class="color" style="left:36px;top:988px"><div class="swatch" style="--c:#9a5ea0"></div><div class="name">azalea /<br><span>azalee</span></div></div>
    <div class="color" style="left:143px;top:988px"><div class="swatch" style="--c:#825aa0"></div><div class="name">iris /<br><span>iris</span></div></div>
    <div class="color" style="left:244px;top:988px"><div class="swatch" style="--c:#c8b3dc"></div><div class="name">lila <span>/ lila</span></div></div>

    <div class="color" style="left:36px;top:1118px"><div class="swatch" style="--c:#8e3c66"></div><div class="name">violet /<br><span>violett</span></div></div>
    <div class="color" style="left:143px;top:1118px"><div class="swatch" style="--c:#9e6174"></div><div class="name">prugna /<br><span>pflaume</span></div></div>

    <div class="color" style="left:36px;top:1242px"><div class="swatch" style="--c:#80687a"></div><div class="name">berry /<br><span>beeren</span></div></div>
    <div class="color" style="left:143px;top:1242px"><div class="swatch" style="--c:#674a4b"></div><div class="name">bronzo /<br><span>bronze</span></div></div>
  </section>

  <section class="cool-colors">
    <div class="color" style="left:946px;top:324px"><div class="swatch" style="--c:#5f5b38"></div><div class="name">olive /<br><span>olive</span></div></div>
    <div class="color" style="left:1071px;top:324px"><div class="swatch" style="--c:#e9f9a3"></div><div class="name">kiwi <span>/ kiwi</span></div></div>
    <div class="color" style="left:1180px;top:324px"><div class="swatch" style="--c:#88dc84"></div><div class="name">verde /<br><span>gron</span></div></div>
    <div class="color" style="left:1286px;top:324px"><div class="swatch" style="--c:#46aa5b"></div><div class="name">grass /<br><span>grassgrin</span></div></div>

    <div class="color" style="left:946px;top:449px"><div class="swatch" style="--c:#a6ecd5"></div><div class="name">aquamarina /<br><span>aquamarina</span></div></div>
    <div class="color" style="left:1071px;top:449px"><div class="swatch" style="--c:#30c9b6"></div><div class="name">Lagoon /<br><span>Lagune</span></div></div>
    <div class="color" style="left:1180px;top:449px"><div class="swatch" style="--c:#5bd8cf"></div><div class="name">Lazur /<br><span>Lazur</span></div></div>
    <div class="color" style="left:1286px;top:449px"><div class="swatch" style="--c:#33ccd5"></div><div class="name">turquoise /<br><span>türkis</span></div></div>

    <div class="color" style="left:946px;top:582px"><div class="swatch" style="--c:#6db7e1"></div><div class="name">blue <span>/ blau</span></div></div>
    <div class="color" style="left:1071px;top:582px"><div class="swatch" style="--c:#bad7f2"></div><div class="name">baby blue /<br><span>baby blau</span></div></div>
    <div class="color" style="left:1180px;top:582px"><div class="swatch" style="--c:#6f6b98"></div><div class="name">jeans /<br><span>jeans</span></div></div>
    <div class="color" style="left:1286px;top:582px"><div class="swatch" style="--c:#4e6a85"></div><div class="name">ocean /<br><span>ozean</span></div></div>
    <div class="color" style="left:1385px;top:582px"><div class="swatch" style="--c:#483a5c"></div><div class="name">night /<br><span>nacht-</span></div></div>

    <div class="color" style="left:946px;top:713px"><div class="swatch" style="--c:#4b3359"></div><div class="name">blu marino /<br><span>blu marino</span></div></div>
    <div class="color" style="left:1092px;top:713px"><div class="swatch" style="--c:#4f3d62"></div><div class="name">blu marino melange /<br><span>blu marino melange</span></div></div>
    <div class="color" style="left:1257px;top:713px"><div class="swatch" style="--c:#413a41"></div><div class="name">denim /<br><span>denim</span></div></div>

    <div class="color" style="left:946px;top:853px"><div class="swatch" style="--c:#61656e"></div><div class="name">silver <span>/ silber-</span></div></div>

    <div class="color" style="left:946px;top:988px"><div class="swatch" style="--c:#806878"></div><div class="name">steel <span>/ stahl-</span></div></div>
    <div class="color" style="left:1091px;top:988px"><div class="swatch" style="--c:#715f63"></div><div class="name">grey /<br><span>grau</span></div></div>
    <div class="color" style="left:1257px;top:988px"><div class="swatch" style="--c:#5b4548"></div><div class="name">graphite /<br><span>graphit</span></div></div>

    <div class="color" style="left:946px;top:1118px"><div class="swatch" style="--c:#4c4c4e"></div><div class="name">smoke <span>/ rauch</span></div></div>
    <div class="color" style="left:1091px;top:1118px"><div class="swatch" style="--c:#414141"></div><div class="name">nero /<br><span>schwarz</span></div></div>
    <div class="color" style="left:1257px;top:1118px"><div class="swatch" style="--c:#4a4a4a"></div><div class="name">nero melange /<br><span>schwarz melange</span></div></div>
  </section>
</main>
</body>
</html>
```